Business card por a urban DJ, up scale audience target

Need a sober design, modern, conservative colors but i can consider some options, y play rnb, hip hop, EDM and top40.

Business card for contact and personal info, double sided, use logo attrached please; im 42 so i need a card acording to my age an target audience.

Target Market(s)

Adult people, up scale audience

Industry/Entity Type

Music Download

Contact Information for Business Card

Cel (574) 3209415586 www.lumaverso.com

Requirements
Must have
• open mind
Nice to have
• open mind
Should not have
• DJ

```html
<!DOCTYPE html>
<html lang="en">
<head>
<meta charset="utf-8">
<title>LUMA business card</title>
<link href="https://fonts.googleapis.com/css2?family=Source+Sans+3:wght@400;600;700&display=swap" rel="stylesheet">
<style>
  :root {
    --ink: #2d2d2d;
    --paper: #ffffff;
    --stage: #e9e7e4;
    --text: #1f1f1f;
  }
  * { margin: 0; padding: 0; box-sizing: border-box; }
  html, body { width: 1200px; height: 900px; overflow: hidden; }
  body {
    background: var(--stage);
    font-family: "Source Sans 3", "Myriad Pro", Arial, sans-serif;
    position: relative;
  }
  .card {
    position: absolute;
    border-radius: 16px;
    overflow: hidden;
    box-shadow: 0 6px 18px rgba(0,0,0,0.18);
  }
  .card--front { left: 78px; top: 34px; width: 588px; height: 364px; background: var(--paper); }
  .card--back { left: 390px; top: 506px; width: 565px; height: 350px; background: var(--ink); }

  .band { position: absolute; }
  .card--front .band { background: var(--ink); top: 64px; height: 99px; }
  .card--front .band--left { left: 0; width: 180px; }
  .card--front .band--right { left: 438px; right: 0; }
  .card--back .band { background: var(--paper); top: 80px; height: 97px; }
  .card--back .band--left { left: 0; width: 162px; }
  .card--back .band--right { left: 400px; right: 0; }

  .brand {
    position: absolute;
    text-align: center;
    font-weight: 700;
    letter-spacing: 4px;
    line-height: 1;
  }
  .card--front .brand { left: 200px; width: 210px; top: 82px; font-size: 62px; color: var(--ink); }
  .card--back .brand { left: 178px; width: 210px; top: 97px; font-size: 62px; color: var(--paper); }

  .identity {
    position: absolute;
    right: 310px;
    top: 228px;
    text-align: right;
    color: var(--text);
    white-space: nowrap;
  }
  .identity__name { font-size: 24px; line-height: 30px; }
  .identity__role { font-size: 16px; line-height: 20px; }
  .identity__address { font-size: 16px; line-height: 19px; margin-top: 10px; }

  .contacts {
    position: absolute;
    left: 318px;
    top: 230px;
    list-style: none;
    color: var(--text);
    font-size: 16px;
    white-space: nowrap;
  }
  .contacts li { display: flex; align-items: center; height: 24.5px; }
  .contacts svg { width: 12px; height: 12px; margin-right: 10px; fill: var(--text); flex: none; }

  .site {
    position: absolute;
    left: 0; right: 0;
    top: 246px;
    text-align: center;
    color: var(--paper);
    font-weight: 700;
    font-size: 17px;
  }
</style>
</head>
<body>
  <section class="card card--front" aria-label="Card front">
    <div class="band band--left"></div>
    <div class="band band--right"></div>
    <div class="brand">LUMA</div>

    <div class="identity">
      <p class="identity__name">Marcus Ellison</p>
      <p class="identity__role">Managing Director</p>
      <p class="identity__address">4820, Harbor Lane Suite<br>Fairview Park, 204519</p>
    </div>

    <ul class="contacts">
      <li><svg viewBox="0 0 12 12"><path d="M2.4 0.5l2 2.2-1 1.3c.8 1.6 2 2.8 3.6 3.6l1.3-1 2.2 2-1.2 1.9C5.4 10.2 1.8 6.6 0.5 1.7z"/></svg>(574) 3209415586</li>
      <li><svg viewBox="0 0 12 12"><path d="M3 1h5v3h3v7H1V4h2zM4 2v2h3V2zM3 6v1h2V6zm3 0v1h2V6zM3 8v1h2V8zm3 0v1h2V8z"/></svg>(574) 3209415587</li>
      <li><svg viewBox="0 0 12 12"><path d="M1 2.5h10v7H1zM1.8 3.3v.4L6 6.6l4.2-2.9v-.4z"/></svg>info@lumaverso.com</li>
      <li><svg viewBox="0 0 12 12"><circle cx="6" cy="6" r="5.5"/><path d="M3 4.5h2l1 1.5-1 1.5 1 2H5L4 7.5 2.8 6z M7 3h2l.5 2H8z" fill="#fff"/></svg>www.lumaverso.com</li>
    </ul>
  </section>

  <section class="card card--back" aria-label="Card back">
    <div class="band band--left"></div>
    <div class="band band--right"></div>
    <div class="brand">LUMA</div>
    <p class="site">www.lumaverso.com</p>
  </section>
</body>
</html>
```